A new business in the finance sector helping asset managers raise assets needs a basic website.

Broadfield Ventures website design brief

SUMMARY
I need a basic website created. The brief includes both designing the website and setting it up via a mainstream website building website like WIX, such that I can edit it and add pages subsequently.

BUSINESS BACKGROUND
Broadfield Ventures Limited is a UK Limited company operating in what we can broadly define as finance. The business has been set up to help various asset management companies with asset raising. These companies are good at managing money but not necessarily good at marketing their skills to prospective investors such as: pension funds, endowments, foundations, family offices and private wealth management groups.

Generally, it is likely that I will carry the card of the firms I am representing so Broadfield Ventures itself won’t be widely used and, as such, I don’t expect the website to get much traffic but it when people do seek to check it out, it needs to convey an image of trustworthiness and professionalism.

For regulatory reasons I won’t be able to do any marketing on the website so this may well end up as a 1 or 2 page website with an introductory page and a bio on me (plus, in time, any others that I choose to partner with or employ) BUT it may be that I can includes some information on the groups I am working with and so I would like the design to allow for me to add pages easily in the future.

MOOD / DESIGN
Asset raising is an important but serious business: integrity, trust and stability are all key. Investors – and particularly the institutional investors that I be speaking to – don’t want anything flashy or trendy; they are looking to build long term relationships and make long term investments. Trustworthiness, longevity, and professionalism are all key.
I am open minded to a more obvious, tried and tested City/Wall Street type design (cue skyscrapers / London City skyline and serious people around a smart board room table) but also interested to explore something that holds to the same values but is more modern.
One of my two initial clients is focused on environmental investment opportunities and I could imagine the winning design wanting to incorporate some reference to that…..although because other managers I work with are not focused on this area, the design cannot be all about that.

WHAT ARE BROADFIELD VENTURES?
A core element of almost any investment strategy – and this is often true in other areas of life too – is to diversify your risk or exposure. In the design world that might mean multiple clients across multiple industries, etc.

In the asset management world (often referred to as money management or fund management), a lot of investments are quite highly correlated, meaning that although they may appear different in some regards, in reality they perform in quite similar ways and especially in times of financial stress such as that experienced in 2007-2009 or, indeed, right now due to Covid.

As such, investors are always interested in finding strategies that offer genuine, reliable diversification where performance is linked to factors unrelated to mainstream financial markets. They may also be interested in some strategies that are negatively correlated to financial markets, meaning they can do well when all around them are doing badly (think of this like having insurance).

Sometimes these strategies offer diversification simply because of what they are invested in (Gold, for example, often does well when stock markets are doing badly as investors seek a safe haven for their money); in other cases it is all about the strategy itself and how it is implemented.
Broadfield Ventures is focused on identifying – and marketing - strategies that really are great diversifiers. Very few firms focus on this area so it is a genuine USP.

LOGO?
Logos for my sort of business are generally frowned upon being considered too flashy. As such, I am unlikely to use one……but the nature of the businesses area of focus (see above) does perhaps lend itself to a logo which has some meaning so I am open-minded to this.

DELIVERABLES
• Website design
• Website built using Wix or equivalent with two initial pages and scope for me to add further pages relating to the groups I am working with.

Happy to answer other questions you may have.

Target Market(s)

Institutional investors like pension funds, endowments, foundations, family offices, sovereign wealth funds, multi-asset managers and private wealth managers

Industry/Entity Type

Finance

Contact Information for Business Card

Glen Mabbott
Broadfield Ventures Limited
Room for telephone number and email address but not address
May need to add regulatory information in due course.

Coding

Coded - Design and coding required

Number of Pages Required

3 page

Font styles to use
Sans Serif

Requirements
Must have
• See project description for mood / design brief. Business is serious: trustworthiness and professionalism are key.
Nice to have
• As per the brief more than one of my clients are in the environmental space so some reference to this would be nice to have....but other clients are not so don't want to give the impression that everything is linked to the environment.
Should not have
• Nothing flashy or gimmicky. The website itself will never be a medium for doing business, rather it is a place people may visit to check me out. They won't spend long there, they key is that the impression they are left with is one of: integrity and professionalism.

```html
<!DOCTYPE html>
<html lang="en">
<head>
<meta charset="utf-8">
<title>Broadfield Ventures Limited</title>
<link href="https://fonts.googleapis.com/css2?family=Lato:wght@400;700;900&display=swap" rel="stylesheet">
<style>
  :root {
    --brand-blue: #0b8bcc;
    --accent-gold: #f2b300;
    --ink: #1f1f1f;
    --muted: #3a3a3a;
    --panel-grey: #f3f3f3;
    --rule: #dcdcdc;
    --white: #ffffff;
  }
  * { box-sizing: border-box; margin: 0; padding: 0; }
  html, body { width: 1200px; height: 4027px; overflow: hidden; }
  body { position: relative; background: var(--white); font-family: 'Lato', sans-serif; color: var(--ink); }
  .abs { position: absolute; }
  .center { text-align: center; }

  /* header */
  .site-header { left: 0; top: 0; width: 1200px; height: 100px; border-bottom: 2px solid var(--rule); }
  .brand-name { left: 76px; top: 32px; font-size: 26px; font-weight: 700; color: var(--brand-blue); }
  .btn-contact { left: 967px; top: 27px; width: 158px; height: 46px; border-radius: 23px; background: var(--accent-gold); color: var(--white); font-size: 18px; font-weight: 700; line-height: 46px; text-align: center; }
  .main-nav { left: 0; top: 100px; width: 1200px; height: 75px; z-index: 2; }
  .main-nav a { position: absolute; top: 26px; font-size: 15px; font-weight: 700; color: var(--ink); text-decoration: none; }
  .main-nav a.active { color: var(--brand-blue); }
  .social-dots { left: 987px; top: 129px; display: flex; gap: 22px; }
  .social-dots span { width: 16px; height: 16px; border-radius: 50%; background: var(--ink); }

  /* hero */
  .hero { left: 0; top: 175px; width: 1200px; height: 637px; background: linear-gradient(180deg, #5d6b7a 0%, #7b8894 35%, #5a6670 65%, #8a8f90 100%); }
  .hero-title { left: 0; top: 374px; width: 1200px; font-size: 58px; font-weight: 900; color: var(--white); }
  .hero-sub { left: 0; top: 450px; width: 1200px; font-size: 25px; line-height: 33px; color: var(--white); }
  .btn-gold { background: var(--accent-gold); color: var(--white); border-radius: 26px; font-weight: 900; text-align: center; letter-spacing: .3px; }
  .hero-btn { left: 508px; top: 550px; width: 182px; height: 52px; font-size: 17px; line-height: 52px; }

  /* about */
  .about { left: 0; top: 812px; width: 1200px; height: 507px; background: var(--brand-blue); }
  .about-photo { left: 616px; top: 812px; width: 509px; height: 507px; background: linear-gradient(135deg, #c9ced3 0%, #8e979e 45%, #3d4650 100%); }
  .about-title { left: 0; top: 930px; width: 660px; font-size: 38px; font-weight: 900; color: var(--white); }
  .about-text { left: 0; top: 1000px; width: 660px; font-size: 17px; line-height: 25px; color: var(--white); }
  .about-btn { left: 236px; top: 1142px; width: 183px; height: 52px; font-size: 17px; line-height: 52px; }

  /* stats */
  .stats { left: 75px; top: 1319px; width: 1050px; height: 326px; background: var(--panel-grey); }
  .stat { width: 200px; top: 1433px; text-align: center; }
  .stat-number { font-size: 52px; font-weight: 900; color: var(--brand-blue); line-height: 1; }
  .stat-label { margin-top: 16px; font-size: 20px; line-height: 27px; color: var(--muted); }

  /* service cards */
  .card-photo { width: 513px; height: 361px; }
  .card-title { width: 513px; font-size: 23px; line-height: 30px; font-weight: 700; color: var(--brand-blue); text-align: center; }
  .card-link { width: 513px; font-size: 16px; font-weight: 700; color: var(--accent-gold); text-align: center; }

  /* focus */
  .focus { left: 0; top: 2825px; width: 1200px; height: 488px; background: var(--brand-blue); color: var(--white); }
  .focus-title { left: 0; top: 2893px; width: 1200px; font-size: 38px; font-weight: 900; color: var(--white); }
  .focus-col { width: 540px; color: var(--white); text-align: center; }
  .focus-col h3 { font-size: 23px; font-weight: 700; margin-bottom: 8px; }
  .focus-col p { font-size: 17px; line-height: 25px; }
  .btn-outline { width: 186px; height: 53px; border: 2px solid var(--white); border-radius: 27px; font-size: 17px; font-weight: 900; line-height: 49px; text-align: center; color: var(--white); }

  /* posts */
  .post { width: 330px; height: 272px; color: var(--white); }
  .post-date { position: absolute; left: 18px; top: 33px; font-size: 15px; }
  .post-title { position: absolute; left: 18px; top: 138px; width: 300px; font-size: 23px; line-height: 32px; }
  .post-rule { position: absolute; left: 0; top: 221px; width: 330px; height: 1px; background: rgba(255,255,255,.6); }
  .post-foot { position: absolute; left: 18px; right: 18px; top: 238px; font-size: 15px; display: flex; justify-content: space-between; }

  /* footer */
  .footer-name { left: 0; top: 3779px; width: 1200px; font-size: 25px; font-weight: 700; }
  .footer-line { left: 0; width: 1200px; font-size: 15px; color: var(--muted); }
</style>
</head>
<body>

<header class="abs site-header">
  <div class="abs brand-name">Broadfield Ventures Limited</div>
  <div class="abs btn-contact">Get InTouch</div>
</header>

<nav class="abs main-nav">
  <a class="active" style="left:77px">Home</a>
  <a style="left:156px">About Us</a>
  <a style="left:259px">Services</a>
  <a style="left:356px">Blog</a>
  <a style="left:427px">Contact Us</a>
</nav>
<div class="abs social-dots" aria-label="Social links"><span></span><span></span><span></span><span></span></div>

<section class="abs hero" role="img" aria-label="City of London skyline with glass towers under a cloudy sky"></section>
<h1 class="abs hero-title center">Broadfield Ventures Limited</h1>
<p class="abs hero-sub center">We are a a UK Limited company operating in what we can<br>broadly define as finance.</p>
<div class="abs btn-gold hero-btn">READ MORE &rsaquo;&rsaquo;</div>

<section class="abs about"></section>
<div class="abs about-photo" role="img" aria-label="Colleagues smiling around a boardroom table"></div>
<h2 class="abs about-title center">ABOUT US</h2>
<p class="abs about-text center">Aliquam non dui enim. Nam vel arcu nec nibh&nbsp; aliquam vulputate.<br>Donec porttitor neque sed enim ultrices iaculis!<br>In quis luctus dolor. Sed ac libero arcuhasellus&nbsp; vulputate<br>ultrices augue, eget feugiat lectus efficitur in.</p>
<div class="abs btn-gold about-btn">READ MORE &rsaquo;&rsaquo;</div>

<section class="abs stats"></section>
<div class="abs stat" style="left:95px"><div class="stat-number">23+</div><div class="stat-label">Pension Funds</div></div>
<div class="abs stat" style="left:298px"><div class="stat-number">540+</div><div class="stat-label">Endowments</div></div>
<div class="abs stat" style="left:502px"><div class="stat-number">32+</div><div class="stat-label">Foundations</div></div>
<div class="abs stat" style="left:705px"><div class="stat-number">52+</div><div class="stat-label">Family Offices</div></div>
<div class="abs stat" style="left:908px"><div class="stat-number">302</div><div class="stat-label">Private Wealth<br>Management</div></div>

<div class="abs card-photo" style="left:73px;top:1711px;background:linear-gradient(135deg,#dfe3e6,#6f7d8c 55%,#2d3a4e)" role="img" aria-label="Business people shaking hands in an office"></div>
<div class="abs card-title" style="left:73px;top:2099px">Nunc eu nunc at<br>venenatis</div>
<div class="abs card-link" style="left:73px;top:2188px">Read More</div>

<div class="abs card-photo" style="left:616px;top:1711px;background:linear-gradient(135deg,#f1ece4,#9a9a98 50%,#2a2b2e)" role="img" aria-label="Trader pointing at market charts on monitors"></div>
<div class="abs card-title" style="left:616px;top:2099px">Nunc eu nunc at<br>venenatis</div>
<div class="abs card-link" style="left:616px;top:2188px">Read More</div>

<div class="abs card-photo" style="left:73px;top:2266px;background:linear-gradient(135deg,#d8d4cf,#5f6670 50%,#1e2430)" role="img" aria-label="Two businessmen reviewing a document beside a laptop"></div>
<div class="abs card-title" style="left:73px;top:2654px">Nunc eu nunc at<br>venenatis</div>
<div class="abs card-link" style="left:73px;top:2743px">Read More</div>

<div class="abs card-photo" style="left:616px;top:2266px;background:linear-gradient(135deg,#3a4150,#8c96a5 50%,#e6ecf2)" role="img" aria-label="Financial reports, calculator and tablet on a desk"></div>
<div class="abs card-title" style="left:616px;top:2654px">Nunc eu nunc at<br>venenatis</div>
<div class="abs card-link" style="left:616px;top:2743px">Read More</div>

<section class="abs focus"></section>
<h2 class="abs focus-title center">Broadfield Ventures is focused on identifying</h2>
<div class="abs focus-col" style="left:60px;top:3005px">
  <h3>Marketing</h3>
  <p>Aliquam non dui enim. Nam vel arcu nec nibh&nbsp; aliquam vulputate.<br>Donec porttitor neque sed enim ultrices iaculis!<br>In quis luctus dolor. Sed ac libero arcuhasellus&nbsp; vulputate<br>ultrices augue, eget feugiat</p>
</div>
<div class="abs focus-col" style="left:601px;top:3005px">
  <h3>Strategies</h3>
  <p>Aliquam non dui enim. Nam vel arcu nec nibh&nbsp; aliquam vulputate.<br>Donec porttitor neque sed enim ultrices iaculis!<br>In quis luctus dolor. Sed ac libero arcuhasellus&nbsp; vulputate<br>ultrices augue, eget feugiat</p>
</div>
<div class="abs btn-outline" style="left:234px;top:3186px">READ MORE &rsaquo;&rsaquo;</div>
<div class="abs btn-outline" style="left:775px;top:3186px">READ MORE &rsaquo;&rsaquo;</div>

<article class="abs post" style="left:75px;top:3403px;background:linear-gradient(135deg,#2c2f36,#4a4e57)" role="img" aria-label="Dim office meeting scene behind blog post">
  <span class="post-date">Aug20 · 1min</span>
  <span class="post-title">Neque porro quisquam est qui dolorem i</span>
  <span class="post-rule"></span>
  <span class="post-foot"><span>Read More</span><span>&#9679; 8 &nbsp;&#9829; 8</span></span>
</article>
<article class="abs post" style="left:436px;top:3403px;background:linear-gradient(135deg,#3a3c40,#5c5f63)" role="img" aria-label="Hands working over paperwork behind blog post">
  <span class="post-date">Aug20 · 1min</span>
  <span class="post-title">Neque porro quisquam est qui dolorem i</span>
  <span class="post-rule"></span>
  <span class="post-foot"><span>Read More</span><span>&#9679; 8 &nbsp;&#9829; 8</span></span>
</article>
<article class="abs post" style="left:797px;top:3403px;background:linear-gradient(135deg,#4a4636,#6a6a6c)" role="img" aria-label="Gold bar on a market chart behind blog post">
  <span class="post-date">Aug20 · 1min</span>
  <span class="post-title">Neque porro quisquam est qui dolorem i</span>
  <span class="post-rule"></span>
  <span class="post-foot"><span>Read More</span><span>&#9679; 8 &nbsp;&#9829; 8</span></span>
</article>

<footer>
  <div class="abs footer-name center">Broadfield Ventures Limited</div>
  <div class="abs footer-line center" style="top:3826px">020-7946-0318</div>
  <div class="abs footer-line center" style="top:3859px">214 Harbour Lane</div>
  <div class="abs footer-line center" style="top:3891px">Millbrook, CA 90210</div>
  <div class="abs footer-line center" style="top:3955px">Copyright &copy; 2020. Broadfield Ventures Limited.All Right Reserved</div>
</footer>

</body>
</html>
```